Corporate Design für QUR Beratung / Entwicklung
Zielgruppe
Freiberufler. QUR Beratung / Entwicklung .
Aufgabenstellung
Slogan:
Your Dedicated Workflow Logic & Operations Automation Partner ( DWLOP )

```html
<!DOCTYPE html>
<html lang="de">
<head>
<meta charset="utf-8">
<title>QUR Beratung / Entwicklung – Geschäftsausstattung</title>
<link rel="stylesheet" href="https://fonts.googleapis.com/css2?family=Manrope:wght@300;400;600;700&display=swap">
<style>
  :root {
    --navy: #2e4470;
    --navy-light: #4766a0;
    --ink: #1a1a1a;
    --muted: #8a8a8a;
    --paper: #f6f6f6;
    --stage: #dcdcde;
    --silver-a: #c9c9c9;
    --silver-b: #9d9d9d;
  }
  * { box-sizing: border-box; margin: 0; padding: 0; }
  html, body { width: 1200px; height: 1200px; overflow: hidden; }
  body {
    background: var(--stage);
    font-family: "Manrope", sans-serif;
    color: var(--ink);
    position: relative;
  }
  .piece { position: absolute; background: var(--paper); box-shadow: 0 1px 4px rgba(0,0,0,.18); }

  /* brand block */
  .brand { display: flex; align-items: center; gap: 6px; }
  .brand-square { width: 12px; height: 12px; background: var(--navy); border-radius: 2px; }
  .brand-name { font-weight: 700; font-size: 20px; letter-spacing: .04em; color: var(--navy); }

  .title { font-size: 6px; font-weight: 400; color: var(--muted); letter-spacing: .02em; text-transform: uppercase; }
  .person { font-size: 12px; font-weight: 600; color: var(--ink); }
  .slogan { font-size: 5px; font-weight: 300; color: var(--muted); text-transform: uppercase; line-height: 1.15; }
  .url { font-size: 5px; font-weight: 700; color: var(--ink); margin-top: 6px; }

  /* letterhead */
  .letterhead { left: 60px; top: 232px; width: 520px; height: 735px; }
  .letterhead .head { position: absolute; right: 38px; top: 26px; text-align: right; display: flex; flex-direction: column; align-items: flex-end; }
  .letterhead .head .title { margin-top: 14px; }
  .letterhead .foot { position: absolute; right: 38px; bottom: 32px; text-align: right; }
  .letterhead .band { position: absolute; left: 0; right: 0; bottom: 0; height: 12px; background: var(--navy); }

  /* envelope */
  .envelope { left: 620px; top: 232px; width: 520px; height: 266px; }
  .envelope .sender { position: absolute; left: 18px; top: 112px; display: flex; align-items: center; gap: 14px; }

  /* business cards */
  .card { width: 250px; height: 162px; padding: 14px; }
  .card .row { display: flex; align-items: center; gap: 10px; }
  .card .info { position: absolute; left: 60px; bottom: 16px; }
  .card-silver { left: 620px; top: 538px; background: linear-gradient(160deg, var(--silver-a) 0%, #b4b4b4 50%, var(--silver-b) 100%); }
  .card-silver .title { color: #6e6e6e; }
  .card-silver .slogan { color: #5e5e5e; }
  .card-navy { left: 890px; top: 538px; background: linear-gradient(165deg, var(--navy-light) 0%, #3b5589 45%, var(--navy) 46%, var(--navy) 100%); color: #fff; text-align: center; display: flex; flex-direction: column; align-items: center; justify-content: flex-end; padding-bottom: 12px; }
  .card-navy .brand { position: absolute; top: 30px; left: 50%; transform: translateX(-50%); }
  .card-navy .brand-square { background: #fff; }
  .card-navy .brand-name { color: #fff; }
  .card-navy .title, .card-navy .slogan { color: #c5cee0; }
  .card-navy .person { color: #fff; margin-bottom: 5px; }
  .card-navy .url { color: #fff; margin-top: 4px; }
  .card-white { left: 620px; top: 720px; background: linear-gradient(165deg, #fbfbfb 0%, #f0f0f0 100%); }
</style>
</head>
<body>

  <section class="piece letterhead">
    <div class="head">
      <div class="brand"><span class="brand-square"></span><span class="brand-name">QUR</span></div>
      <p class="title">Dipl.Ing.(FH)</p>
      <p class="person">Markus Feldhahn</p>
    </div>
    <div class="foot">
      <p class="slogan">Your Dedicated Workflow Logic<br>&amp; Operations Automation Partner ( DWLOP )</p>
      <p class="url">DWLOP.DE</p>
    </div>
    <div class="band"></div>
  </section>

  <section class="piece envelope">
    <div class="sender">
      <div class="brand"><span class="brand-square"></span><span class="brand-name">QUR</span></div>
      <div>
        <p class="title">Dipl.Ing.(FH)</p>
        <p class="person">Markus Feldhahn</p>
      </div>
    </div>
  </section>

  <section class="piece card card-silver">
    <div class="row">
      <div class="brand"><span class="brand-square"></span><span class="brand-name">QUR</span></div>
      <div>
        <p class="title">Dipl.Ing.(FH)</p>
        <p class="person">Markus Feldhahn</p>
      </div>
    </div>
    <div class="info">
      <p class="slogan">Your Dedicated Workflow Logic<br>&amp; Operations Automation Partner ( DWLOP )</p>
      <p class="url">DWLOP.DE</p>
    </div>
  </section>

  <section class="piece card card-navy">
    <div class="brand"><span class="brand-square"></span><span class="brand-name">QUR</span></div>
    <p class="title">Dipl.Ing.(FH)</p>
    <p class="person">Markus Feldhahn</p>
    <p class="slogan">Your Dedicated Workflow Logic<br>&amp; Operations Automation Partner ( DWLOP )</p>
    <p class="url">DWLOP.DE</p>
  </section>

  <section class="piece card card-white">
    <div class="row">
      <div class="brand"><span class="brand-square"></span><span class="brand-name">QUR</span></div>
      <div>
        <p class="title">Dipl.Ing.(FH)</p>
        <p class="person">Markus Feldhahn</p>
      </div>
    </div>
    <div class="info">
      <p class="slogan">Your Dedicated Workflow Logic<br>&amp; Operations Automation Partner ( DWLOP )</p>
      <p class="url">DWLOP.DE</p>
    </div>
  </section>

</body>
</html>
```